Awesome Digital Ad Design – Pellucid Adreach

I am going to be setting up a Pellucid Adreach ad campaign I need creatives for.

Several sizes are needed in the end, however, please submit your design concept in the following 2 sizes to start:
Medium rectangle: 300X250
Leaderboard: 728X90

Original artwork/design files and images used expected upon payment and as part of the final delivery.

Ads should match our company brand and the information on this webpage: http://www.harborlyneworks.com/real-estate-marketing/
SEE MORE INSTRUCTIONS IN ATTACHED WORD DOC
Updates

Target Market(s)

Business-To-Business Audience –Real Estate Company Executives (Presidents/VPs/Owners/CEOs/Sales Managers).

Industry/Entity Type

Real Estate

Font styles to use
Sans Serif

Requirements
Must have
• Copy should be minimal words, billboard like. Please use real photos/images that would appeal to real estate high-level decision-maker executives.
Should not have
• No cartoons or graphics

```html
<!DOCTYPE html>
<html lang="en">
<head>
<meta charset="utf-8">
<title>Harborlyne Works – Pellucid Adreach Banners</title>
<link href="https://fonts.googleapis.com/css2?family=Jost:wght@400;500;600&display=swap" rel="stylesheet">
<style>
  :root {
    --page-bg: #ececec;
    --white: #ffffff;
    --navy: #0c2340;
    --scene-light: #7880a6;
    --scene-dark: #4d557c;
    --headline-gold: #f1da8c;
    --cta-orange: #ec650f;
    --cta-orange-dark: #c84f08;
    --logo-ink: #1c2230;
    --logo-dot: #7a2a3a;
    --panel-shade: #b9bccb;
  }
  * { box-sizing: border-box; margin: 0; padding: 0; }
  html, body { width: 1200px; height: 874px; overflow: hidden; }
  body {
    background: var(--page-bg);
    font-family: "Jost", sans-serif;
    position: relative;
  }
  .banner {
    position: absolute;
    overflow: hidden;
    transform-origin: 0 0;
    transform: scale(1.093);
    background: var(--navy);
  }
  .banner--rectangle { width: 300px; height: 250px; left: 433px; top: 143px; }
  .banner--leaderboard { width: 728px; height: 90px; left: 199px; top: 521px; }

  .scene {
    position: absolute;
    background: linear-gradient(135deg, var(--scene-light), var(--scene-dark));
  }
  .banner--rectangle .scene { left: 0; top: 0; width: 300px; height: 125px; }
  .banner--leaderboard .scene { left: 0; top: 0; width: 590px; height: 90px; }

  .logo-panel { position: absolute; left: 0; top: 0; }
  .brand {
    position: absolute;
    display: flex; align-items: center; gap: 5px;
    color: var(--logo-ink);
    font-weight: 500;
    font-size: 11px;
    line-height: 1.1;
  }
  .brand__dot { width: 7px; height: 7px; border-radius: 50%; background: var(--logo-dot); flex: none; }
  .banner--rectangle .brand { left: 10px; top: 40px; }
  .banner--leaderboard .brand { left: 16px; top: 34px; }

  .message { position: absolute; text-align: center; text-transform: none; }
  .message__kicker { color: var(--headline-gold); font-weight: 600; font-size: 20px; line-height: 1; letter-spacing: 0.2px; }
  .message__headline { color: var(--white); font-weight: 600; font-size: 28px; line-height: 1.05; }
  .message__tagline { color: var(--white); font-weight: 400; font-size: 12px; line-height: 1.2; margin-top: 2px; }
  .banner--rectangle .message { left: 0; width: 300px; top: 132px; }
  .banner--leaderboard .message { left: 150px; width: 270px; top: 11px; }

  .cta {
    position: absolute;
    display: flex; align-items: center; justify-content: center; text-align: center;
    background: linear-gradient(180deg, var(--cta-orange), var(--cta-orange-dark));
    color: var(--white);
    font-weight: 500;
    border-radius: 4px;
    box-shadow: 0 1px 3px rgba(0,0,0,0.35);
  }
  .banner--rectangle .cta { left: 91px; top: 204px; width: 118px; height: 36px; font-size: 15px; }
  .banner--leaderboard .cta { left: 601px; top: 9px; width: 110px; height: 71px; font-size: 24px; line-height: 1.02; border-radius: 6px; }

  .cta-panel { position: absolute; left: 576px; top: 0; }
</style>
</head>
<body>

  <section class="banner banner--rectangle" aria-label="Medium rectangle ad 300 by 250">
    <div class="scene" role="img" aria-label="Photo of a small wooden figure climbing steps while a hand places the next step"></div>
    <svg class="logo-panel" width="300" height="250" viewBox="0 0 300 250" aria-hidden="true">
      <polygon points="0,0 134,0 0,125" fill="var(--panel-shade)"/>
      <polygon points="0,0 127,0 0,122" fill="var(--white)"/>
      <polygon points="250,125 258,116 266,125" fill="var(--navy)"/>
    </svg>
    <div class="brand"><span class="brand__dot"></span><span>Harborlyne<br>Works</span></div>
    <div class="message">
      <p class="message__kicker">CLIENT FOLLOW-UP</p>
      <p class="message__headline">MADE SIMPLE</p>
      <p class="message__tagline">Virtually No Cost To Your Company!</p>
    </div>
    <a class="cta">LEARN MORE</a>
  </section>

  <section class="banner banner--leaderboard" aria-label="Leaderboard ad 728 by 90">
    <div class="scene" role="img" aria-label="Photo of a small wooden figure climbing steps while a hand places the next step"></div>
    <svg class="logo-panel" width="728" height="90" viewBox="0 0 728 90" aria-hidden="true">
      <polygon points="0,0 146,0 98,90 0,90" fill="var(--panel-shade)"/>
      <polygon points="0,0 140,0 92,90 0,90" fill="var(--white)"/>
    </svg>
    <svg class="cta-panel" width="152" height="90" viewBox="0 0 152 90" aria-hidden="true">
      <polygon points="10,0 152,0 152,90 10,90 10,26 0,16 10,6" fill="var(--navy)"/>
    </svg>
    <div class="brand"><span class="brand__dot"></span><span>Harborlyne<br>Works</span></div>
    <div class="message">
      <p class="message__kicker">CLIENT FOLLOW-UP</p>
      <p class="message__headline">MADE SIMPLE</p>
      <p class="message__tagline">Virtually No Cost To Your Company!</p>
    </div>
    <a class="cta">LEARN<br>MORE</a>
  </section>

</body>
</html>
```